Web Design Project - Management Consulting Firm Firm

We need a design to upgrade our website. The design should reflect the core values , branding of the firm & must be benchmarked with the best management consulting firms in the world.

It should have right choice of images , have evoke words / captions that will attract traffic & must be the best design for a contemporary management consulting firm

current website - www.tallbirchwood.biz
Updates

Hello Designers

we are keen to take our website to next level. It should be benchmarked with best management consulting firm's website on look and feel..

i have uploaded the corporate profile ,  mkt strategy..

email me for any clarifications..

Good Luck

Vikas

Project Deadline Extended
Reason: We want the best Design!! and we want to extend the deadline by 3 more days.. 10 Days to go..

Any takers??

Target Market(s)

CFO / CIO / CEO / Business owners & Decision makers

Industry/Entity Type

Management Consulting

Requirements
Must have
• Lively ; but not flashy or flamboyant.

It should reflect the brand values / TBW positioning that I will be sharing .

Benchmark and compare with the best consulting firm websites

Nice to have
• Images..but nothing flashy..

benchmark with leading consulting firms websites..
1.norvitane
2.Pravelle
3. Harwick Advisory Group
4. Tilden & Crowe
5. Fairloch
6. Voss Consulting
Should not have
• Too loud.

```html
<!DOCTYPE html>
<html lang="en">
<head>
<meta charset="utf-8">
<title>TBW – About Us</title>
<link href="https://fonts.googleapis.com/css2?family=Source+Sans+3:ital,wght@0,300;0,400;0,600;0,700;1,400&display=swap" rel="stylesheet">
<style>
:root{
  --navy:#2b2d72;
  --red:#c9230f;
  --cream:#fffdf7;
  --grey-text:#7d7d7d;
  --side-bg:#f0f3f6;
  --side-active:#b3c1ca;
  --footer:#626268;
  --rule:#dcdcdc;
  --icon-fill:rgba(255,255,255,.22);
}
*{box-sizing:border-box;margin:0;padding:0}
html,body{width:1104px;height:1200px;overflow:hidden;background:#fff;font-family:"Source Sans 3",sans-serif}
.page{position:relative;width:1104px;height:1200px}
.abs{position:absolute}
a{color:inherit;text-decoration:none}

/* header */
.logo{left:196px;top:14px;font-size:52px;line-height:56px;font-weight:600;color:var(--navy);letter-spacing:1px}
.phone{left:647px;top:19px;font-size:14px;color:var(--red)}
.util-links{left:786px;top:19px;font-size:9.9px;font-style:italic;color:var(--navy)}
.util-links span{margin:0 4px}
.search{left:817px;top:79px;width:115px;height:17px;background:#f1f1f1;border:1px solid #e6e6e6}
.search em{position:absolute;left:7px;top:1px;font-size:9px;color:#aaa}
.search-btn{position:absolute;right:0;top:0;width:19px;height:15px;background:#d4d4d4}

/* nav */
.main-nav{left:29px;top:115px;width:1046px;height:38px;background:var(--navy);box-shadow:0 2px 4px rgba(0,0,0,.3)}
.nav-item{position:absolute;top:0;height:38px;line-height:38px;text-align:center;color:#fff;font-size:13px;font-weight:700;border-right:1px solid #23255f;white-space:nowrap}
.nav-item.active{background:var(--red)}

/* hero */
.hero{left:29px;top:153px;width:1046px;height:211px;background:linear-gradient(100deg,#b2a596 0%,#d8c6b6 30%,#c9a794 55%,#8c9cae 80%,#9db1c7 100%)}
.hero-caption{left:245px;top:204px;width:287px;height:97px;background:rgba(120,110,100,.55);color:#fff;font-size:18px;line-height:30px;padding:6px 0 0 158px;white-space:nowrap;overflow:hidden}
.dropdown{left:155px;top:153px;width:252px;height:179px;background:var(--red)}
.dropdown-list{position:absolute;left:9px;top:11px;width:235px;height:153px;background:var(--cream);border-radius:4px;list-style:none;padding:0 12px}
.dropdown-list li{font-size:12px;font-weight:600;color:var(--navy);border-bottom:1px solid #e3ded3;height:33px;padding-top:12px}
.dropdown-list li:last-child{border:0;height:auto;line-height:19px;padding-top:6px}

/* services */
.service{top:403px;height:117px;background:var(--navy);color:#fff;text-align:center}
.service-icon{display:block;width:40px;height:70px;margin:9px auto 0;background:var(--icon-fill)}
.service h2{font-weight:300;font-size:21px;line-height:26px;margin-top:2px}

/* sidebar */
.sidebar{left:29px;top:563px;width:303px;height:524px;background:var(--side-bg)}
.side-menu{left:155px;top:563px;width:177px;list-style:none}
.side-menu li{position:relative;border-bottom:1px solid var(--rule);font-size:9.8px;font-weight:600;color:var(--navy);padding:0 0 0 8px;display:flex;align-items:center}
.side-menu li::after{content:"›";position:absolute;right:10px;font-size:13px;color:#999}
.side-menu li.active{background:var(--side-active);color:#fff;font-size:10.8px}
.side-menu li.active::after{color:var(--navy)}
.brochure{left:159px;top:742px;width:152px;height:28px;border:1px solid #d3d3d3;border-radius:2px;background:#f8f8f8;display:flex;font-size:10.3px;font-weight:700;color:#888}
.brochure b{background:var(--red);color:#fff;width:29px;display:flex;align-items:center;justify-content:center;font-size:9.5px}
.brochure span{display:flex;align-items:center;padding-left:6px;white-space:nowrap}

/* content */
.content-title{left:383px;top:557px;font-size:24.5px;font-weight:600;color:var(--navy)}
.content-lead{left:384px;top:603px;font-size:18px;font-weight:600;color:#8a8a8a;white-space:nowrap}
.content-photo{left:783px;top:650px;width:163px;height:130px;border:2px solid #d8d8d8;background:linear-gradient(135deg,#4a5450,#1c2120 60%,#333)}
.values{left:381px;top:646px;width:580px;list-style:none}
.values h3{font-size:10.5px;font-weight:600;color:var(--navy)}
.values p{font-size:10.5px;color:var(--grey-text);line-height:16px;margin-top:3px}

/* footer */
.footer{left:29px;top:1106px;width:1046px;height:94px;background:var(--footer);color:#eee}
.footer-links{position:absolute;left:0;right:0;top:14px;text-align:center;font-size:8.8px;white-space:nowrap}
.footer-links span{margin:0 6px;color:#ccc}
.subscribe{position:absolute;left:137px;top:51px;width:216px;height:27px;background:#fff;border:3px solid #ddd;font-size:9px;color:#444;padding:5px 0 0 9px;white-space:nowrap}
.subscribe i{position:absolute;right:5px;top:4px;width:13px;height:13px;border-radius:50%;background:#aaa}
.social{position:absolute;top:55px;width:19px;height:19px;background:#8fa3c4}
.legal{position:absolute;right:142px;top:47px;font-size:10.8px;white-space:nowrap}
.legal span{margin:0 5px;color:#ccc}
.copy{position:absolute;left:680px;top:78px;font-size:9px;white-space:nowrap}
</style>
</head>
<body>
<div class="page">

  <header>
    <div class="abs logo">TBW</div>
    <div class="abs phone">T: +971 4 5550123</div>
    <nav class="abs util-links">Media Room<span>|</span>Contact Us<span>|</span>Insights</nav>
    <div class="abs search"><em>Search</em><div class="search-btn"></div></div>
  </header>

  <nav class="abs main-nav">
    <a class="nav-item active" style="left:126px;width:82px">ABOUT US</a>
    <a class="nav-item" style="left:208px;width:84px">OUR TEAM</a>
    <a class="nav-item" style="left:292px;width:166px">FUNCTIONAL PRACTISES</a>
    <a class="nav-item" style="left:458px;width:150px">INDUSTRY PRACTISES</a>
    <a class="nav-item" style="left:608px;width:101px">OUR CLIENTS</a>
    <a class="nav-item" style="left:709px;width:106px">CASE STUDIES</a>
    <a class="nav-item" style="left:815px;width:94px">CONTACT US</a>
  </nav>

  <div class="abs hero" role="img" aria-label="Photo of clasped hands in teamwork"></div>
  <div class="abs hero-caption">fast growing<br>e</div>
  <div class="abs dropdown">
    <ul class="dropdown-list">
      <li>About us</li>
      <li>Core Philosophies</li>
      <li>Alliances</li>
      <li>Unique Value – Combining tech-<br>strategy-finance</li>
    </ul>
  </div>

  <section>
    <div class="abs service" style="left:158px;width:211px">
      <span class="service-icon" role="img" aria-label="Strategy consulting icon"></span>
      <h2>Strategy Consulting</h2>
    </div>
    <div class="abs service" style="left:447px;width:209px">
      <span class="service-icon" role="img" aria-label="Process consulting icon"></span>
      <h2>Process Consulting</h2>
    </div>
    <div class="abs service" style="left:732px;width:215px">
      <span class="service-icon" role="img" aria-label="Technology icon"></span>
      <h2>Technology</h2>
    </div>
  </section>

  <aside>
    <div class="abs sidebar"></div>
    <ul class="abs side-menu">
      <li class="active" style="height:32px">About us</li>
      <li style="height:33px">Core Philosophies</li>
      <li style="height:33px">Alliances</li>
      <li style="height:48px;line-height:14px">Unique Value –<br>Combining tech-strategy-finance</li>
    </ul>
    <div class="abs brochure"><b>PDF</b><span>DOWNLOAD BROCHURE</span></div>
  </aside>

  <main>
    <h1 class="abs content-title">About Us</h1>
    <p class="abs content-lead">To use our intellectual capital to transform our client's business.</p>
    <div class="abs content-photo" role="img" aria-label="Photo of a businessman drawing a rising growth line"></div>
    <ul class="abs values">
      <li style="height:57px"><h3>&nbsp;Transparency, Integrity and Good Sense</h3><p>To have sound governance, be ethical and display good sense in all our dealings</p></li>
      <li style="height:75px"><h3>Fairness</h3><p>To be objective, play by the rules, meet our contractual obligations,<br>charge honestly for our services and thereby earn trust and respect</p></li>
      <li style="height:56px"><h3>Client Confidentiality</h3><p>To not disclose sensitive client information even if it means furthering our own interests</p></li>
      <li style="height:70px"><h3>Pursuit of Excellence</h3><p>To achieve excellence through constant learning and investment in ourselves, innovation and agility and consistently<br>delivering results beyond customer expectations</p></li>
      <li style="height:56px"><h3>Leadership</h3><p>To demonstrate professional leadership and high standards and be a role model for the industry</p></li>
      <li><h3>Teamwork</h3><p>To create within the organization a culture of sharing of knowledge and ideas, mutual respect, courtesy and comaraderie.<br>Teamwork brings out best solutions.</p></li>
    </ul>
  </main>

  <footer class="abs footer">
    <nav class="footer-links">ABOUT US<span>|</span>OUR TEAM<span>|</span>FUNCTIONAL PRACTISES<span>|</span>INDUSTRY PRACTISES<span>|</span>OUR CLIENTS<span>|</span>CASE STUDIES<span>|</span>MEDIA ROOM<span>|</span>CONTACT US<span>|</span>INSIGHTS</nav>
    <div class="subscribe">Enter email for Latest updates &amp; News<i></i></div>
    <div class="social" style="left:364px"></div>
    <div class="social" style="left:388px"></div>
    <div class="social" style="left:412px"></div>
    <div class="social" style="left:436px"></div>
    <nav class="legal">Help<span>|</span>Site Map<span>|</span>Privacy<span>|</span>Terms &amp; Conditions</nav>
    <div class="copy">© 2013 TBW, All Rights Reserved</div>
  </footer>

</div>
</body>
</html>
```